CONTEMPORARY Canva Art Design for Christians

I need a canvas art design on Christianity. The design must be in 3 SIMPLE dimensions: 12x 18 inches / 28 x 24 inches / 30 x 40 inches
The design must be accompanied by christian quote.
The christian quote can be "As For Me And My House We Will Serve The Lord (Joshua 24:15)" or any other quote that is good for display in a christian home.

I DON'T WANT THE TRADITIONAL CHRISTIAN DESIGN.. I WANT COLOURFUL, MEANINGFUL and CONTEMPORARY, MODERN DESIGN. And stay away from the scary image of Jesus in dark background, it only makes the home more scary not holy!

Target Market(s)

Christians

Colors

Designer to choose colors to be used in the design.

Requirements
Must have
• A graphic design and a christian quote that is powerful and edifies the soul. Great for display at home. Great use of colours to enhance the message.
Nice to have
• I wish to see great unique design with strong use of colours, images to enhance the scripture. It must glorify Jesus.
Should not have
• Should not be dull.

```html
<!DOCTYPE html>
<html lang="en">
<head>
<meta charset="utf-8">
<title>As For Me And My House – Canvas Art</title>
<link rel="stylesheet" href="https://fonts.googleapis.com/css2?family=Tinos:wght@400;700&family=Roboto+Condensed:wght@300&display=swap">
<style>
  :root {
    --page-bg: #e4e4e4;
    --sky-deep: #0a2fa8;
    --sky-mid: #2f74d6;
    --sky-light: #9fcdf2;
    --glow: #ffffff;
    --ink: #050505;
  }
  html, body {
    margin: 0;
    padding: 0;
    width: 1200px;
    height: 1200px;
    overflow: hidden;
    background: var(--page-bg);
  }
  .canvas-art {
    position: absolute;
    left: 0;
    top: 200px;
    width: 1200px;
    height: 800px;
    display: block;
  }
  .verse {
    font-family: "Tinos", "Times New Roman", serif;
    fill: var(--ink);
    text-anchor: middle;
  }
  .verse-ref {
    font-family: "Roboto Condensed", "Arial Narrow", sans-serif;
    font-weight: 300;
    fill: #1a1a2a;
    text-anchor: middle;
  }
</style>
</head>
<body>
<svg class="canvas-art" viewBox="0 0 1200 800" xmlns="http://www.w3.org/2000/svg">
  <defs>
    <radialGradient id="skyGlow" cx="611" cy="170" r="820" gradientUnits="userSpaceOnUse">
      <stop offset="0" stop-color="var(--glow)"/>
      <stop offset="0.22" stop-color="#f2f8fd"/>
      <stop offset="0.45" stop-color="var(--sky-light)"/>
      <stop offset="0.72" stop-color="var(--sky-mid)"/>
      <stop offset="1" stop-color="var(--sky-deep)"/>
    </radialGradient>
    <radialGradient id="cloudHaze" cx="600" cy="560" r="520" gradientUnits="userSpaceOnUse">
      <stop offset="0" stop-color="#ffffff" stop-opacity="0.35"/>
      <stop offset="1" stop-color="#ffffff" stop-opacity="0"/>
    </radialGradient>
  </defs>

  <g class="sky-scene" role="img" aria-label="Bright blue sky with sun rays breaking through clouds and a white dove descending in front of a glowing cross">
    <rect width="1200" height="800" fill="url(#skyGlow)"/>
    <rect width="1200" height="800" fill="url(#cloudHaze)"/>
    <g class="glow-cross" fill="#ffffff" opacity="0.55">
      <rect x="588" y="61" width="46" height="209"/>
      <rect x="469" y="161" width="281" height="47"/>
    </g>
  </g>

  <g class="quote">
    <text class="verse" x="627" y="388" font-size="63">As For Me And</text>
    <text class="verse" x="627" y="464"><tspan font-size="52">My </tspan><tspan font-size="74">House</tspan></text>
    <text class="verse" x="627" y="534" font-size="54">We Will</text>
    <text class="verse" x="627" y="604" font-size="52">Serve The</text>
    <text class="verse" x="627" y="731" font-size="158" textLength="442" lengthAdjust="spacingAndGlyphs">LORD</text>
    <text class="verse-ref" x="627" y="773" font-size="27">(JOSHUA 24:15)</text>
  </g>
</svg>
</body>
</html>
```